Business Card for Multi-Brand Sportswear Company

We are looking for a business card which represents our company and the multiple brands within it.

The company: Kelt Athletic (LTD)
The brands: Kelt, PawaLuni, VerdantFlex, Grit and Gale

Employees using these cards would be representing Kelt Athletic, rather than any of the individual brands. You will see a current design within the uploaded files, to give some inspiration. The actual text of the brands is not necessary, but the logos should be on there is some format.

Our creative minds on this are stretched, so we are looking for someone to make this their own, and show us what a good business card should look like.

We may like to get these printed with spot gloss, so keep that in mind with your designs.

www.keltathletic.co.uk

Industry/Entity Type

Business

Contact Information for Business Card

Tom Hollingsworth-Pryce
Operations Manager
(+44) 1632 960 418
Tom@keltathletic.co.uk
www.keltathletic.co.uk

Font styles to use
Sans Serif
Other font styles liked:
• Eurostile

Colors
ffffff

Requirements
Nice to have
• Dark (black) background

```html
<!DOCTYPE html>
<html lang="en">
<head>
<meta charset="utf-8">
<title>Kelt Athletic – Business Card</title>
<link rel="stylesheet" href="https://fonts.googleapis.com/css2?family=Michroma&family=Open+Sans:wght@400;600&family=Oswald:wght@600&display=swap">
<style>
  :root {
    --backdrop: #8a8a8a;
    --card-black: #000000;
    --accent-red: #e3232b;
    --band-grey: #4a4a4c;
    --text-white: #ffffff;
    --logo-silver: #bdbdbd;
    --card-w: 560px;
    --card-h: 320px;
  }
  * { box-sizing: border-box; margin: 0; padding: 0; }
  html, body { width: 1200px; height: 1000px; overflow: hidden; }
  body {
    background: radial-gradient(ellipse at 50% 40%, #a9a9a9 0%, var(--backdrop) 70%);
    position: relative;
    font-family: "Open Sans", sans-serif;
    color: var(--text-white);
  }
  .card {
    position: absolute;
    width: var(--card-w);
    height: var(--card-h);
    background: var(--card-black);
    border-radius: 28px;
    overflow: hidden;
    box-shadow: 0 14px 30px rgba(0,0,0,0.35);
  }
  .card--front { left: 110px; top: 110px; }
  .card--back { left: 530px; top: 560px; }

  /* front */
  .strip { position: absolute; left: 0; right: 0; height: 20px; display: flex; }
  .strip--top { top: 0; }
  .strip--bottom { bottom: 0; }
  .strip__red { background: var(--accent-red); }
  .strip__grey { background: var(--band-grey); }
  .strip--top .strip__red { width: 55%; }
  .strip--top .strip__grey { flex: 1; }
  .strip--bottom .strip__grey { width: 45%; }
  .strip--bottom .strip__red { flex: 1; }

  .brandmark {
    position: absolute; inset: 0;
    display: flex; flex-direction: column; align-items: center; justify-content: center;
  }
  .brandmark__name {
    font-family: "Michroma", sans-serif;
    font-size: 30px;
    letter-spacing: 2px;
    color: var(--logo-silver);
  }
  .brandmark__tagline {
    margin-top: 6px;
    font-family: "Open Sans", sans-serif;
    font-size: 10px;
    letter-spacing: 3px;
    color: var(--logo-silver);
  }

  /* back */
  .brand-row {
    position: absolute; left: 0; right: 0; top: 80px;
    display: flex; justify-content: center; gap: 22px;
    font-family: "Michroma", sans-serif;
    font-size: 12px;
    color: var(--logo-silver);
  }
  .contact-panel {
    position: absolute; right: 0; top: 172px; bottom: 28px; width: 48%;
    background: var(--accent-red);
    padding: 14px 16px;
    font-size: 11.5px;
    line-height: 1.55;
  }
  .contact-panel__address { margin-bottom: 2px; }
  .contact-line { display: flex; align-items: center; gap: 8px; }
  .contact-line svg { width: 11px; height: 11px; flex: none; }
  .name-panel {
    position: absolute; left: 0; top: 214px; bottom: 28px; width: 52%;
    background: var(--band-grey);
    display: flex; flex-direction: column; justify-content: center;
    padding-left: 36px;
  }
  .name-panel__name {
    font-family: "Oswald", sans-serif;
    font-weight: 600;
    font-size: 26px;
    letter-spacing: 0.5px;
    line-height: 1.1;
  }
  .name-panel__role { font-size: 13px; margin-left: 30px; }
</style>
</head>
<body>

<section class="card card--front" aria-label="Card front">
  <div class="strip strip--top"><div class="strip__red"></div><div class="strip__grey"></div></div>
  <div class="brandmark">
    <span class="brandmark__name">KELT ATHLETIC</span>
    <span class="brandmark__tagline">PERFORMANCE WEAR</span>
  </div>
  <div class="strip strip--bottom"><div class="strip__grey"></div><div class="strip__red"></div></div>
</section>

<section class="card card--back" aria-label="Card back">
  <div class="brand-row">
    <span class="brand-row__item">Grit and Gale</span>
    <span class="brand-row__item">VerdantFlex</span>
    <span class="brand-row__item">Kelt</span>
    <span class="brand-row__item">PawaLuni</span>
  </div>

  <div class="contact-panel">
    <div class="contact-panel__address">Fern Court, Harlow Vale, Ashby, AB12 3CD</div>
    <div class="contact-line">
      <svg viewBox="0 0 24 24" aria-hidden="true"><path fill="#fff" d="M6.6 10.8a15 15 0 0 0 6.6 6.6l2.2-2.2a1 1 0 0 1 1-.25 11.4 11.4 0 0 0 3.6.57 1 1 0 0 1 1 1V20a1 1 0 0 1-1 1A17 17 0 0 1 3 4a1 1 0 0 1 1-1h3.5a1 1 0 0 1 1 1c0 1.25.2 2.45.57 3.57a1 1 0 0 1-.25 1z"/></svg>
      <span>+44(0)1632 960418</span>
    </div>
    <div class="contact-line">
      <svg viewBox="0 0 24 24" aria-hidden="true"><rect x="2" y="5" width="20" height="14" fill="#fff"/><path d="M2 5l10 8 10-8" fill="none" stroke="#e3232b" stroke-width="2"/></svg>
      <span>dan@keltathletic.co.uk</span>
    </div>
    <div class="contact-line">
      <svg viewBox="0 0 24 24" aria-hidden="true"><circle cx="12" cy="12" r="10" fill="#fff"/><path d="M2 12h20M12 2c3 3 3 17 0 20M12 2c-3 3-3 17 0 20" fill="none" stroke="#e3232b" stroke-width="1.5"/></svg>
      <span>www.keltathletic.co.uk</span>
    </div>
  </div>

  <div class="name-panel">
    <div class="name-panel__name">DAN ASHCOMBE</div>
    <div class="name-panel__role">Managing Director</div>
  </div>
</section>

</body>
</html>
```